Illustration Design Project

I have an existing illustration I have written up, I need it professionally redone, perhaps as an infographic or new design from the current layout.

Pls plan for a few edits and revisions.

I will need it large enough to be made into a wall poster size.

```html
<!DOCTYPE html>
<html lang="en">
<head>
<meta charset="utf-8">
<title>Accountable vs. Complacency</title>
<link rel="stylesheet" href="https://fonts.googleapis.com/css2?family=Cinzel:wght@400;700&family=Patrick+Hand&display=swap">
<style>
  :root {
    --bg: #a8a8a8;
    --ornament: #959595;
    --ink: #2a2a2a;
    --ink-soft: #3a3a3a;
    --orange: #ee8a3a;
    --orange-deep: #d9691c;
    --orange-light: #fbe0c4;
    --oval-rim: #2b2926;
    --oval-glow: #f4f1d4;
    --oval-edge: #5b5843;
    --cream: #f7f3df;
  }
  html, body {
    margin: 0;
    padding: 0;
    overflow: hidden;
    background: var(--bg);
  }
  .poster {
    position: relative;
    width: 900px;
    height: 1200px;
    overflow: hidden;
    background: var(--bg);
  }
  .poster__ornament {
    position: absolute;
    inset: 0;
    background:
      radial-gradient(ellipse 320px 260px at 450px 230px, rgba(140,140,140,0.45), transparent 70%),
      radial-gradient(ellipse 360px 300px at 450px 980px, rgba(140,140,140,0.45), transparent 70%),
      radial-gradient(ellipse 260px 420px at 120px 760px, rgba(145,145,145,0.35), transparent 70%),
      radial-gradient(ellipse 260px 420px at 800px 760px, rgba(145,145,145,0.35), transparent 70%),
      var(--bg);
  }
  .poster__art {
    position: absolute;
    inset: 0;
  }
  .subtitle {
    font-family: Arial, Helvetica, sans-serif;
    font-style: italic;
    font-size: 11px;
    fill: var(--ink);
  }
  .pole-title {
    font-family: "Cinzel", serif;
    font-size: 40px;
    fill: var(--ink);
    letter-spacing: 1px;
  }
  .pole-rule {
    stroke: var(--ink);
    stroke-width: 1.6;
  }
  .step-label {
    font-family: "Cinzel", serif;
    font-size: 19px;
    fill: var(--ink-soft);
    letter-spacing: 0.5px;
  }
  .step-quote {
    font-family: "Patrick Hand", cursive;
    font-size: 20px;
    fill: var(--ink);
    letter-spacing: 1px;
  }
  .step-number {
    font-family: "Cinzel", serif;
    font-weight: 700;
    font-size: 28px;
    fill: #1a1a1a;
  }
  .step-badge {
    fill: url(#badgeFill);
    stroke: var(--orange-deep);
    stroke-width: 1;
  }
  .arrow-line {
    fill: none;
    stroke: var(--orange);
    stroke-width: 14;
  }
  .arrow-head { fill: var(--orange); }
  .centre-rim { fill: var(--oval-rim); }
  .centre-face { fill: url(#ovalGlow); }
  .centre-title {
    font-family: "Cinzel", serif;
    font-size: 52px;
    fill: var(--cream);
    stroke: #1f1d19;
    stroke-width: 1.2;
    paint-order: stroke;
  }
</style>
</head>
<body>
<main class="poster">
  <div class="poster__ornament" role="img" aria-label="Faint grey floral scroll ornament across the background"></div>

  <svg class="poster__art" width="900" height="1200" viewBox="0 0 900 1200">
    <defs>
      <radialGradient id="badgeFill" cx="45%" cy="35%" r="65%">
        <stop offset="0%" stop-color="var(--orange-light)"/>
        <stop offset="45%" stop-color="#f6b173"/>
        <stop offset="100%" stop-color="var(--orange-deep)"/>
      </radialGradient>
      <radialGradient id="ovalGlow" cx="50%" cy="45%" r="60%">
        <stop offset="0%" stop-color="var(--oval-glow)"/>
        <stop offset="60%" stop-color="#c9c6a4"/>
        <stop offset="100%" stop-color="var(--oval-edge)"/>
      </radialGradient>
    </defs>

    <!-- Header -->
    <text class="subtitle" x="450" y="55" text-anchor="middle">Accountable vs. Complacency</text>
    <text class="pole-title" x="451" y="108" text-anchor="middle">ACCOUNTABLE</text>
    <line class="pole-rule" x1="309" y1="114" x2="593" y2="114"/>

    <!-- Upward arrow -->
    <path class="arrow-line" d="M455,530 C446,500 446,480 449,463 C452,440 440,420 443,402 C446,375 452,360 450,339 C452,310 458,295 458,275 C458,250 457,220 457,160"/>
    <polygon class="arrow-head" points="457,125 498,165 416,165"/>

    <!-- Downward arrow -->
    <path class="arrow-line" d="M457,680 C460,705 452,720 455,741 C456,770 444,790 446,809 C448,840 452,855 452,876 C454,900 460,912 460,930 C461,960 464,980 463,996 C464,1010 466,1025 466,1040"/>
    <polygon class="arrow-head" points="466,1077 505,1038 427,1038"/>

    <!-- Accountable steps -->
    <g class="step">
      <circle class="step-badge" cx="458" cy="211" r="22"/>
      <text class="step-number" x="458" y="221" text-anchor="middle">5</text>
      <text class="step-label" x="428" y="217" text-anchor="end">GETS ON WITH IT</text>
      <text class="step-quote" x="488" y="218">“ O.K. ,let’s do it ! “</text>
    </g>
    <g class="step">
      <circle class="step-badge" cx="458" cy="275" r="22"/>
      <text class="step-number" x="458" y="285" text-anchor="middle">4</text>
      <text class="step-label" x="426" y="281" text-anchor="end">FINS SOLUTION</text>
      <text class="step-quote" x="490" y="282">“ What can I do ? “</text>
    </g>
    <g class="step">
      <circle class="step-badge" cx="450" cy="339" r="22"/>
      <text class="step-number" x="450" y="349" text-anchor="middle">3</text>
      <text class="step-label" x="418" y="347" text-anchor="end">OWNS IT</text>
      <text class="step-quote" x="482" y="346">“ If it’s to be, it’s up to me ! “</text>
    </g>
    <g class="step">
      <circle class="step-badge" cx="443" cy="402" r="22"/>
      <text class="step-number" x="443" y="412" text-anchor="middle">2</text>
      <text class="step-label" x="409" y="409" text-anchor="end">ACKNOWLEDGES</text>
      <text class="step-label" x="409" y="435" text-anchor="end">REALITY</text>
      <text class="step-quote" x="475" y="406">“ This is the way it is. “</text>
    </g>
    <g class="step">
      <circle class="step-badge" cx="449" cy="463" r="22"/>
      <text class="step-number" x="449" y="473" text-anchor="middle">1</text>
      <text class="step-label" x="415" y="472" text-anchor="end">SEEKS REALITY</text>
      <text class="step-quote" x="481" y="468">“ What’s happening ? “</text>
    </g>

    <!-- Centre -->
    <g class="centre">
      <ellipse class="centre-rim" cx="450" cy="603" rx="194" ry="89"/>
      <ellipse class="centre-face" cx="450" cy="603" rx="178" ry="75" role="img" aria-label="Dark swirl ornament inside the glowing oval"/>
      <text class="centre-title" x="450" y="598" text-anchor="middle">LIFE</text>
      <text class="centre-title" x="450" y="650" text-anchor="middle">HAPPENS</text>
    </g>

    <!-- Victim steps -->
    <g class="step">
      <circle class="step-badge" cx="455" cy="741" r="22"/>
      <text class="step-number" x="455" y="751" text-anchor="middle">1</text>
      <text class="step-label" x="425" y="749" text-anchor="end">AVOIDS REALITY</text>
      <text class="step-quote" x="487" y="745">“ Ask no questions. “</text>
    </g>
    <g class="step">
      <circle class="step-badge" cx="446" cy="809" r="22"/>
      <text class="step-number" x="446" y="819" text-anchor="middle">2</text>
      <text class="step-label" x="417" y="818" text-anchor="end">FIGHTS REALITY</text>
      <text class="step-quote" x="477" y="816">“ That’s not how I see it. “</text>
    </g>
    <g class="step">
      <circle class="step-badge" cx="452" cy="876" r="22"/>
      <text class="step-number" x="452" y="886" text-anchor="middle">3</text>
      <text class="step-label" x="420" y="884" text-anchor="end">BLAMES</text>
      <text class="step-quote" x="484" y="878">“ If everyone would just</text>
      <text class="step-quote" x="513" y="912">do their job ! “</text>
    </g>
    <g class="step">
      <circle class="step-badge" cx="460" cy="930" r="22"/>
      <text class="step-number" x="460" y="940" text-anchor="middle">4</text>
      <text class="step-label" x="304" y="939">PERSONAL</text>
      <text class="step-label" x="304" y="965">EXCUSES</text>
      <text class="step-quote" x="492" y="934">“ It’s not my job. “</text>
    </g>
    <g class="step">
      <circle class="step-badge" cx="463" cy="996" r="22"/>
      <text class="step-number" x="463" y="1006" text-anchor="middle">5</text>
      <text class="step-label" x="427" y="1004" text-anchor="end">WAITS : HOPES</text>
      <text class="step-quote" x="494" y="1000">“ If it was meant to be,</text>
      <text class="step-quote" x="514" y="1033">it’ll happen. “</text>
    </g>

    <!-- Footer -->
    <text class="pole-title" x="452" y="1134" text-anchor="middle">VICTIM</text>
    <line class="pole-rule" x1="366" y1="1140" x2="538" y2="1140"/>
  </svg>
</main>
</body>
</html>
```